Travel video blogger needs website design

I need a website designed for my new travel video blog "Roaming Sparrow". I have only just started but need a website that is fairly simple and not too busy. I have a logo which I want on it (I have attached it to this project). I also want a link to all my other social medias on the main page (vidtrekhub, Snapwell and Palnook) and my videos as well. Here is a link to my vidtrekhub page for you to look at: https://www.vidtrekhub.net/channel/QRm4tZ8pWnE2HX57YKccd31v
As I have only just started and I am still trying to find my specific niche, again I need it to be sleek and simple that I can go in and change slightly here and there. I would like these pages on the website: About Me, Videos, Social Media, Blog, Gallery, contact me. for an example I like the look of www.theroamingkinfolk.net website.

I already have the domain and I am with Harborweb with pagecraftr.org. I just want to spend my time getting better and learning about videos then trying to create a website (I am a bit of a perfectionist when I try to do something).

Target Market(s)

Young Adults (majority females) between the ages of 18 and 30 with an interest in travelling.

Industry/Entity Type

Travel Industry

Number of Pages Required

1 page

Colors

Designer to choose colors to be used in the design.

Requirements
Must have
• A like to my Snapwell, Palnook and vidtrekhub channels on the home page
• Must be a nice, simple design
• Must have my logo on the front and name "Roaming Sparrow"
Nice to have
• A nice light, bright coloured theme
Should not have
• A dark coloured theme

```html
<!DOCTYPE html>
<html lang="en">
<head>
<meta charset="utf-8">
<title>Roaming Sparrow — Videos</title>
<link rel="stylesheet" href="https://fonts.googleapis.com/css2?family=Lato:wght@400;700;900&display=swap">
<style>
  :root {
    --page-bg: #ffffff;
    --ink: #1a1a1a;
    --tile-text: #ffffff;
    --dusk-top: #c98a5e;
    --dusk-bottom: #2e2422;
    --neon-a: #1f3f44;
    --neon-b: #7a8f86;
    --tokyo-a: #c9475a;
    --tokyo-b: #1e5a5c;
    --tokyo-c: #0d2424;
    --sunny-a: #f2b640;
    --sunny-b: #e9e6e1;
    --terra-a: #d99a5c;
    --terra-b: #8cb6c9;
    --road-a: #1c1c1e;
    --road-b: #a9b3b6;
  }
  * { box-sizing: border-box; margin: 0; padding: 0; }
  html, body { width: 1200px; height: 1200px; overflow: hidden; background: var(--page-bg); }
  body { position: relative; font-family: "Lato", sans-serif; color: var(--ink); }

  .site-header .welcome {
    position: absolute; left: 206px; top: 86px;
    font-size: 9.5px; letter-spacing: 0.2px;
  }
  .brand {
    position: absolute; left: 540px; top: 78px; width: 120px;
    display: flex; flex-direction: column; align-items: center; gap: 8px;
  }
  .brand-mark { width: 48px; height: 48px; border: 1.5px solid var(--ink); border-radius: 50%; }
  .brand-name { font-size: 12px; font-weight: 700; letter-spacing: 1.5px; text-transform: uppercase; white-space: nowrap; }

  .social-links {
    position: absolute; right: 210px; top: 86px;
    display: flex; gap: 18px; list-style: none; font-size: 10px; font-weight: 700;
  }
  .social-links a { color: var(--ink); text-decoration: none; }

  .main-nav {
    position: absolute; left: 376px; top: 200px; width: 425px;
    display: flex; justify-content: space-between; font-size: 9.5px;
  }
  .main-nav a { color: var(--ink); text-decoration: none; }
  .main-nav .active { font-weight: 700; }

  .tile {
    position: absolute; display: flex; align-items: center; justify-content: center; overflow: hidden;
  }
  .tile-title {
    color: var(--tile-text); font-weight: 900; font-size: 27px; letter-spacing: -0.5px;
    text-shadow: 0 1px 4px rgba(0,0,0,0.45); text-transform: uppercase;
  }
  .tile-title.large { font-size: 34px; }

  .dusk { background: linear-gradient(180deg, #8a7468 0%, var(--dusk-top) 40%, #5a3a33 62%, var(--dusk-bottom) 100%); }
  .neon { background: linear-gradient(160deg, var(--neon-a) 0%, var(--neon-b) 45%, #3b3a2c 75%, #1a1e1c 100%); }
  .tokyo { background: linear-gradient(120deg, var(--tokyo-a) 0%, #d7a06a 22%, #6fb5b0 45%, var(--tokyo-b) 70%, var(--tokyo-c) 100%); }
  .sunny { background: linear-gradient(135deg, var(--sunny-b) 0%, var(--sunny-a) 40%, #f4c45a 65%, #e8e4e6 100%); }
  .terra { background: linear-gradient(110deg, var(--terra-a) 0%, #e6c79a 35%, var(--terra-b) 55%, #c58a5c 100%); }
  .road { background: linear-gradient(90deg, var(--road-a) 0%, #3a3d40 22%, var(--road-b) 50%, #6e7270 75%, var(--road-a) 100%); }

  .player-controls { position: absolute; left: 0; right: 0; bottom: 0; height: 24px; }
</style>
</head>
<body>
  <header class="site-header">
    <p class="welcome">WELCOME!</p>
    <div class="brand">
      <span class="brand-mark"></span>
      <span class="brand-name">Roaming Sparrow</span>
    </div>
    <ul class="social-links">
      <li><a href="#">Snapwell</a></li>
      <li><a href="#">Palnook</a></li>
      <li><a href="https://www.vidtrekhub.net/channel/QRm4tZ8pWnE2HX57YKccd31v">vidtrekhub</a></li>
    </ul>
    <nav class="main-nav">
      <a href="#">About me</a><span>/</span>
      <a href="#" class="active">Videos</a><span>/</span>
      <a href="#">Social Media</a><span>/</span>
      <a href="#">Blog</a><span>/</span>
      <a href="#">Gallery</a><span>/</span>
      <a href="#">Contact Me</a>
    </nav>
  </header>

  <main class="video-grid">
    <a class="tile dusk" style="left:167px;top:246px;width:199px;height:176px" role="img" aria-label="Mountain range under a dusky orange sky"><span class="tile-title">Poland</span></a>
    <a class="tile neon" style="left:389px;top:246px;width:199px;height:176px" role="img" aria-label="Rainy city street with lit shop signs at night"><span class="tile-title">Shanghai</span></a>
    <div class="tile road" style="left:610px;top:246px;width:422px;height:176px" role="img" aria-label="Video still: mountains seen through a car windscreen">
      <svg class="player-controls" viewBox="0 0 422 24" width="422" height="24">
        <polygon points="22,6 22,16 31,11" fill="#fff"/>
        <line x1="58" y1="11" x2="394" y2="11" stroke="rgba(255,255,255,0.55)" stroke-width="2"/>
        <circle cx="170" cy="11" r="3" fill="#fff"/>
      </svg>
    </div>

    <a class="tile tokyo" style="left:167px;top:446px;width:611px;height:370px" role="img" aria-label="Neon-lit street crossing with passing cars at night"><span class="tile-title large">Tokyo Streets</span></a>
    <a class="tile sunny" style="left:803px;top:446px;width:229px;height:176px" role="img" aria-label="Flat lay of a striped shirt, keyboard and travel gadgets"><span class="tile-title">Top 10 Items</span></a>
    <a class="tile terra" style="left:803px;top:646px;width:229px;height:170px" role="img" aria-label="Sunlit old town street with balconies"><span class="tile-title">Italiano</span></a>

    <a class="tile dusk" style="left:167px;top:842px;width:199px;height:176px" role="img" aria-label="Mountain range under a dusky orange sky"><span class="tile-title">Poland</span></a>
    <a class="tile neon" style="left:389px;top:842px;width:199px;height:176px" role="img" aria-label="Rainy city street with lit shop signs at night"><span class="tile-title">Shanghai</span></a>
    <a class="tile road" style="left:610px;top:842px;width:422px;height:176px" role="img" aria-label="Mountains seen through a car windscreen"><span class="tile-title">Road Trip</span></a>

    <a class="tile tokyo" style="left:167px;top:1042px;width:611px;height:370px" role="img" aria-label="Neon-lit street crossing with passing cars at night"></a>
    <a class="tile sunny" style="left:803px;top:1042px;width:229px;height:176px" role="img" aria-label="Flat lay of a striped shirt, keyboard and travel gadgets"><span class="tile-title">Top 10 Items</span></a>
  </main>
</body>
</html>
```